Fort 12 - Mellow Ridge Foundation Case for Support

I am looking to turn this PowerPoint into a Case for Support leave behind booklet - ideally 16-24 pages.

This booklet will be ask for financial support for a Capita Campaign 5 million dollar project

Target Market(s)

Donors - https://mellowridgesfoundation-sample.com/ is our website

Requirements
Must have
• Brochure that can be left behind
Nice to have
• Lots of pictures easy to read font

```html
<!DOCTYPE html>
<html lang="en">
<head>
<meta charset="utf-8">
<title>Fort 12 – Mellow Ridge Foundation Case for Support</title>
<link href="https://fonts.googleapis.com/css2?family=Montserrat:wght@700;800&family=Lato:wght@400;700&display=swap" rel="stylesheet">
<style>
  :root{
    --navy:#1d3b6c;
    --gold:#e0a12a;
    --ink:#2e2e2e;
    --rule:#d9d9d9;
    --paper:#ffffff;
    --bg:#ffffff;
  }
  *{box-sizing:border-box;margin:0;padding:0}
  html,body{width:1200px;height:531px;overflow:hidden;background:var(--bg)}
  body{position:relative;font-family:'Lato',sans-serif;color:var(--ink)}
  .page{position:absolute;top:14px;width:387px;height:500px;background:var(--paper);
        border:1px solid var(--rule);overflow:hidden}
  .page--cover{left:6px}
  .page--intro{left:406px}
  .page--about{left:806px}
  .page__accent{position:absolute;left:0;top:0;bottom:0;width:4px;background:var(--gold)}
  .abs{position:absolute}
  .body-text{font-size:6.7px;line-height:10.6px;text-align:justify}
  .page-title{font-family:'Montserrat',sans-serif;font-weight:800;color:var(--navy);font-size:16px;letter-spacing:.3px;line-height:1;white-space:nowrap}
  .page-title--long{font-size:14.4px;letter-spacing:.2px}
  .page-number{position:absolute;right:8px;bottom:6px;font-size:6.5px}
  .photo{position:absolute}

  /* cover */
  .cover__frame{position:absolute;left:8px;top:6px;width:373px;height:488px;border:1px solid #222;pointer-events:none}
  .cover__photo{left:0;top:0;width:387px;height:305px;
     background:linear-gradient(180deg,#a9a9a9 0%,#6d6d6d 45%,#3e3e3e 75%,#575757 100%)}
  .cover__brand{position:absolute;left:16px;top:40px;font-family:'Lato',sans-serif;font-weight:700;
     font-size:12px;color:var(--navy);letter-spacing:.3px}
  .cover__title{position:absolute;left:0;right:0;top:323px;text-align:center;font-family:'Montserrat',sans-serif;
     font-weight:800;font-size:17px;line-height:20px;color:var(--navy)}
  .cover__title span{color:#2a2a2a}
  .cover__tagline{position:absolute;left:0;right:0;top:380px;text-align:center;color:var(--gold);font-weight:700;font-size:9px}
  .cover__lead{position:absolute;left:20px;right:20px;top:401px;text-align:center;font-size:6.8px;line-height:10.6px}
  .contact{position:absolute;left:20px;top:449px;font-size:6.8px;line-height:12.2px}
  .contact li{list-style:none;display:flex;align-items:center;gap:5px}
  .contact li:first-child{font-weight:700}
  .contact svg{width:7px;height:7px;flex:none}
  .presenter{position:absolute;left:281px;top:437px;font-size:6.8px;line-height:10.8px}
  .presenter__label{color:var(--navy);font-weight:700;margin-bottom:4px}
  .presenter strong{font-weight:700}

  /* bullets */
  .bullets{list-style:none}
  .bullets li{position:relative;padding-left:14px;font-size:6.7px;line-height:10.6px;text-align:justify;margin-bottom:7px}
  .bullets li svg{position:absolute;left:0;top:1px;width:8px;height:8px}

  .subhead{font-weight:700;font-size:7.6px;color:#222}
</style>
</head>
<body>

<!-- Cover -->
<section class="page page--cover">
  <div class="photo cover__photo" role="img" aria-label="Black and white photograph of a wooden guard tower beside a barbed-wire fence under a cloudy sky"></div>
  <div class="cover__brand">Mellow Ridge</div>
  <div class="cover__frame"></div>
  <h1 class="cover__title">Restoring Canada’s Historic WWII<br><span>Prisoner-of-War Camp</span></h1>
  <p class="cover__tagline">Preserve History. Protect Legacy. Reimagine the Future.</p>
  <p class="cover__lead">Fort 12 stands as one of Canada’s most significant surviving World War II heritage sites.<br>Today, this historic landmark faces urgent restoration needs — and your support can help protect its stories, architecture, and legacy for generations to come.</p>
  <ul class="contact">
    <li><svg viewBox="0 0 10 10"><path d="M5 0a3.5 3.5 0 0 0-3.5 3.5C1.5 6 5 10 5 10s3.5-4 3.5-6.5A3.5 3.5 0 0 0 5 0zm0 5a1.4 1.4 0 1 1 0-2.8A1.4 1.4 0 0 1 5 5z" fill="#111"/></svg>Dana Whitfield Founder, Brightpath Giving Inc.</li>
    <li><svg viewBox="0 0 10 10"><path d="M2 .5l2 2-1 1.3a6 6 0 0 0 3.2 3.2L7.5 6l2 2-1.2 1.5C4.5 9.5.5 5.5.5 1.7z" fill="#111"/></svg>(555) 010-2-22</li>
    <li><svg viewBox="0 0 10 10"><rect x=".5" y="2" width="9" height="6" fill="#111"/><path d="M.5 2L5 5.5 9.5 2" stroke="#fff" stroke-width=".8" fill="none"/></svg>dana@brightpathgiving-sample.com</li>
  </ul>
  <div class="presenter">
    <p class="presenter__label">Presented By</p>
    <p><strong>The Mellow Ridge Foundation</strong></p>
    <p>In Partnership with</p>
    <p><strong>Brightpath Giving Inc.</strong></p>
  </div>
</section>

<!-- Introduction -->
<section class="page page--intro">
  <div class="page__accent"></div>
  <h2 class="page-title abs" style="left:15px;top:35px">INTRODUCTION</h2>
  <div class="photo" style="left:193px;top:11px;width:180px;height:146px;background:linear-gradient(180deg,#5f8a3a 0%,#7ea24c 35%,#8c8078 60%,#2f3440 100%)" role="img" aria-label="Colour photograph of a weathered historic brick building with a chimney surrounded by trees"></div>
  <p class="body-text abs" style="left:15px;top:53px;width:166px">The Mellow Ridge Foundation (MRF), in partnership with Brightpath Giving Inc., embarked in July 2025 on a comprehensive process to design a capital campaign that will help preserve one of Canada’s most historically significant sites: Fort 12, the former World War II prisoner-of-war camp in Brookhaven. This plan reflects months of collaboration, discovery, and strategic analysis to determine the most effective path to raise $1.45 million in public and individual philanthropy,</p>
  <p class="body-text abs" style="left:15px;top:170px;width:358px">Since July 2025, Brightpath Giving has engaged directly with members of the Mellow Ridge Foundation Board, key volunteers, and community partners to assess the organization’s campaign readiness and uncover opportunities to mobilize support at scale. This work has included:</p>
  <div class="photo" style="left:15px;top:214px;width:171px;height:163px;background:linear-gradient(180deg,#e9e9e9 0%,#bdbdbd 45%,#5a5a5a 75%,#8a8a8a 100%)" role="img" aria-label="Archival black and white photograph of a two-storey brick building with a chimney"></div>
  <ul class="bullets abs" style="left:194px;top:218px;width:179px">
    <li><svg viewBox="0 0 10 10"><circle cx="5" cy="5" r="5" fill="#444"/><path d="M2.5 5h4M5 3l2 2-2 2" stroke="#fff" stroke-width="1" fill="none"/></svg>Conducting multiple discovery meetings with MRF leadership, board members, and volunteer champions</li>
    <li><svg viewBox="0 0 10 10"><circle cx="5" cy="5" r="5" fill="#444"/><path d="M2.5 5h4M5 3l2 2-2 2" stroke="#fff" stroke-width="1" fill="none"/></svg>Reviewing stakeholder engagement findings led by partners such as Slate Bridge Partners, including public consultation summaries and community use data</li>
    <li><svg viewBox="0 0 10 10"><circle cx="5" cy="5" r="5" fill="#444"/><path d="M2.5 5h4M5 3l2 2-2 2" stroke="#fff" stroke-width="1" fill="none"/></svg>Analyzing campaign-related materials such as donor recognition policies, communication assets, historical reports, budget documents, architectural information, community engagement insights, and operational frameworks</li>
    <li><svg viewBox="0 0 10 10"><circle cx="5" cy="5" r="5" fill="#444"/><path d="M2.5 5h4M5 3l2 2-2 2" stroke="#fff" stroke-width="1" fill="none"/></svg>Assessing early fundraising practices, donor tracking systems, and gift-in-kind processes to identify strengths and gaps</li>
  </ul>
  <p class="body-text abs" style="left:15px;top:395px;width:358px">Through this work, one truth became immediately clear: the movement to save Fort 12 has already begun. Public attention, advocacy efforts, and widespread community support have collectively created a powerful launchpad for a national campaign – one that is rooted in history, remembrance, and the preservation of a rare cultural landmark.</p>
  <p class="body-text abs" style="left:15px;top:438px;width:358px">This Capital Campaign Plan leverages that momentum. It outlines a strategy to raise $1.45 million in public and individual giving, forming the philanthropic foundation required to advance stabilization efforts and unlock further investment through government grants, corporate partners, and in-kind contributors. The plan is designed to position Fort 12 not only as a local heritage site, but as a national legacy project - one worthy of protection, storytelling, and collective stewardship.</p>
  <span class="page-number">2</span>
</section>

<!-- About -->
<section class="page page--about">
  <div class="page__accent"></div>
  <h2 class="page-title page-title--long abs" style="left:15px;top:36px">ABOUT THE MELLOW RIDGE FOUNDATION</h2>
  <p class="body-text abs" style="left:15px;top:56px;width:358px">The Mellow Ridge Foundation (MRF) is a volunteer-led, registered non-profit charity based in Elmstead, Ontario. Since its incorporation in 2014, the Foundation has devoted itself to preserving, protecting, and sharing the layered history of Fort 12 (formerly the Brookhaven Boys’ Training School and a WWII prisoner-of-war camp). Through heritage stewardship, public education, and community engagement, MRF works in partnership with the Municipality of Elmstead, local heritage organizations, and volunteer advocates to safeguard this nationally significant site for present and future generations.</p>
  <h3 class="subhead abs" style="left:15px;top:119px">Mission, Vision &amp; Values</h3>
  <p class="body-text abs" style="left:15px;top:137px;width:358px">A Bold Mission: To rejuvenate a Canadian historic and architecturally significant site in Elmstead, Ontario (Fort 12) for reuse by international, national, and local audiences; and to preserve its complex heritage of having served both as a reform school and as a prisoner-of-war camp, while integrating sensitively and meaningfully with the Brookhaven community.</p>
  <p class="body-text abs" style="left:15px;top:184px;width:358px">A Clear Vision: A future in which Fort 12 stands not only as a preserved historic landmark, but as a vibrant hub for education, remembrance, community gathering, cultural programming, and public engagement - ensuring the site’s stories, architecture, and legacy are honored, shared, and woven into the fabric of community identity.</p>
  <div class="photo" style="left:15px;top:231px;width:172px;height:187px;background:linear-gradient(160deg,#8fae6a 0%,#6f9a48 40%,#7a9a55 70%,#a8a89a 100%)" role="img" aria-label="Aerial view of a scale model of the camp grounds with red brick buildings and paths across green lawns"></div>
  <ul class="bullets abs" style="left:197px;top:238px;width:176px">
    <li><svg viewBox="0 0 10 10"><circle cx="5" cy="5" r="5" fill="#444"/><path d="M2.5 5h4M5 3l2 2-2 2" stroke="#fff" stroke-width="1" fill="none"/></svg>Preservation &amp; Respect for History: Recognizing the importance of safeguarding tangible and intangible heritage, honoring both the institutional and wartime chapters of the site’s past.</li>
    <li><svg viewBox="0 0 10 10"><circle cx="5" cy="5" r="5" fill="#444"/><path d="M2.5 5h4M5 3l2 2-2 2" stroke="#fff" stroke-width="1" fill="none"/></svg>Community Integration: Committing to thoughtful reuse that harmonizes with the surrounding community of Brookhaven, fostering shared ownership and local</li>
    <li><svg viewBox="0 0 10 10"><circle cx="5" cy="5" r="5" fill="#444"/><path d="M2.5 5h4M5 3l2 2-2 2" stroke="#fff" stroke-width="1" fill="none"/></svg>Education &amp; Public Engagement: Promoting understanding of the site’s layered history through tours, research, public programming, and outreach.</li>
    <li><svg viewBox="0 0 10 10"><circle cx="5" cy="5" r="5" fill="#444"/><path d="M2.5 5h4M5 3l2 2-2 2" stroke="#fff" stroke-width="1" fill="none"/></svg>Transparency &amp; Accountability: Ensuring that donations, preservation efforts, and stewardship decisions are conducted openly and responsibly, with 100% of public gifts directed toward restoration, education, and programming.</li>
  </ul>
  <p class="body-text abs" style="left:15px;top:438px;width:358px">Collaboration &amp; Partnership: Working closely with municipal authorities, local heritage organizations, volunteers, historians, and community stakeholders to bring a shared vision to life. Over the last decade, the Mellow Ridge Foundation has laid the groundwork for long-term preservation and renewal of Fort 12. Key strategic milestones and focus areas have included: Heritage Recognition &amp; Protection: Fort 12’s designation as a national historic site (2013) and subsequent heritage-designation of six major buildings and cultural foundation for preservation.</p>
  <span class="page-number">3</span>
</section>

</body>
</html>
```